Gestaltung Flyer & Infokärtchen für Tellerbund
Zielgruppe
Hungrige Personen im Geschäft/Firma (keine Privatpersonen zu Hause), welche Menüs bestellen wollen. Die Menüs dürfen nicht zuviel kosten, aber der Flyer darf deshalb auch nicht "billig" daher kommen. Im Gegenteil.
Aufgabenstellung
Tellerbund - Deine Food Community ist eine seite, die virtuelle Bestellgemeinschaften schafft und damit Lieferpauschalen und Mindestbestellmengen für den Einzelbesteller umgeht. Der Einzelbesteller kennt also seine "Mitbesteller" nicht. Zudem wird das Menü günstiger, je mehr Leute in seiner Community bestellen. Diese Mitbesteller sind andere Personen in der gleichen Firma oder direkte Nachbarfirmen. In jedem Fall geht es um Bestellung von warmen Menüs.
Enorm wichtig und absolut zentral bei dem Infoflyer A4 UND dem kleinen Infokärtchen (A6 gefaltet mit aussen hinten weiss, aussen vorne Hauptmessage mit Logo (seperater Wettbewerb) und Innen zentrale Messages mit Internetseite www.TBM.ch) ist:
1. Der zentrale Unterschied zu anderen Bestellsystemen. warum der Kunde bei uns bestellen soll. Aus 2 Gründen!
1. "Keine Lieferpauschale", "Keine Mindestbestellmenge", "Punkte sammeln". Keine Lieferpauschale und keine Mindestbestellmenge - auch wenn nur 1 Menü bestellt wird. Bei Jedem Kauf kann der Besteller Punkte sammeln und diese dann in gratis Menü umwandeln. Zudem sammelt auch die virtuelle Bestellgemeinschaft punkte. Bei Erreichen von xy Punkten wird in der Community Preise verlost.
2. Community Gedanke: Je mehr bestellt wird, desto günstiger wird der Preis - bis zu einem bestimmten Minimum. Bei ersten Besteller kostet also bspw. das Menü warm geliefert all inkl. 15 Euro; bis minimum 9 Euro. Es muss aber voraus bezahlt werden (diese info muss aber ncht unbedingt auch drauf).
Beispiele für den Community Gedanken wären:
- "Tellerbund - Deine Food Community - Je mehr bestellen, desto günstiger wird’s"
- "Tellerbund - Deine Food Community - Andere bestellen - Du profitierst"
- "Tellerbund - Deine Food Community - Du bist teil der Community - mehr Besteller - günstiger Preis" etc.
- oder man stellt dies bildlich dar zusammen bspw. mit text 1 (ich stelle mir bspw. vor, 1 männchen hoher Preis ($ oben auf berg) und..

```html
<!DOCTYPE html>
<html lang="de">
<head>
<meta charset="utf-8">
<title>Tellerbund – Flyer</title>
<link rel="stylesheet" href="https://fonts.googleapis.com/css2?family=PT+Sans:wght@400;700&family=Patrick+Hand&display=swap">
<style>
  :root {
    --page-bg: #ffffff;
    --frame-orange: #e0801f;
    --text-orange: #e07a14;
    --brand-blue: #4a84c4;
    --sky-top: #d6e6f3;
    --sky-bottom: #ffffff;
    --plate-white: #fbfbfb;
    --button-top: #c3d99a;
    --button-bottom: #98ba64;
    --food-light: #eadbb8;
    --food-green: #5f9a3a;
    --cursor-grey: #e4e4e4;
  }
  * { margin: 0; padding: 0; box-sizing: border-box; }
  html, body { width: 1200px; height: 1200px; overflow: hidden; background: var(--page-bg); }
  .flyer {
    position: absolute; left: 170px; top: 30px; width: 788px; height: 1112px;
    background: linear-gradient(180deg, var(--sky-top) 0%, #e9f1f8 35%, var(--sky-bottom) 62%);
    border-left: 10px solid var(--frame-orange);
    border-bottom: 10px solid var(--frame-orange);
    box-shadow: 6px 6px 14px rgba(0,0,0,.25);
    overflow: hidden;
    font-family: "PT Sans", Arial, sans-serif;
  }
  .frame-top { position: absolute; left: 0; top: 0; width: 330px; height: 10px; background: var(--frame-orange); }
  .frame-right { position: absolute; right: 0; top: 340px; width: 12px; bottom: 0; background: var(--frame-orange); }
  .plate {
    position: absolute; left: 307px; top: -176px; width: 516px; height: 516px; border-radius: 50%;
    background: radial-gradient(circle at 50% 45%, #ffffff 60%, #f0f0f0 100%);
    box-shadow: -2px 4px 10px rgba(0,0,0,.08);
  }
  .brand {
    position: absolute; left: 445px; top: 128px; display: flex; align-items: center; gap: 12px;
    font-size: 38px; font-weight: 700; color: var(--brand-blue);
  }
  .brand-dot { width: 26px; height: 26px; border-radius: 50%; background: var(--frame-orange); }
  .headline { position: absolute; color: var(--brand-blue); font-size: 39px; line-height: 1; white-space: nowrap; }
  .headline strong { font-size: 74px; font-weight: 700; }
  .headline-one { left: 48px; top: 342px; }
  .headline-two { left: 118px; top: 412px; }
  .benefits { position: absolute; left: 50px; top: 548px; list-style: none; }
  .benefits li {
    display: flex; align-items: center; gap: 12px; height: 57px;
    font-family: "Patrick Hand", "Comic Sans MS", cursive; font-size: 30px; color: var(--text-orange);
  }
  .benefits svg { width: 24px; height: 24px; }
  .cta {
    position: absolute; left: 100px; top: 725px; width: 248px; height: 63px; border-radius: 8px;
    background: linear-gradient(180deg, var(--button-top), var(--button-bottom));
    box-shadow: 0 3px 6px rgba(0,0,0,.25);
    color: #fff; font-size: 29px; display: flex; align-items: center; justify-content: center;
  }
  .cta-pointer { position: absolute; left: 306px; top: 768px; width: 34px; height: 52px; }
  .food-photo {
    position: absolute; left: 0; top: 840px; width: 470px; height: 235px;
    border-radius: 0 120px 40px 0;
    background: linear-gradient(100deg, var(--food-green) 0%, #8fc060 22%, var(--food-light) 40%, #d9bf8c 75%, rgba(255,255,255,0) 100%);
  }
  .pointer-crowd {
    position: absolute; left: 420px; top: 830px; width: 356px; height: 272px;
    background: linear-gradient(160deg, rgba(255,255,255,0) 10%, var(--cursor-grey) 70%);
  }
  .web-address { position: absolute; left: 48px; top: 1070px; font-size: 23px; color: var(--brand-blue); }
</style>
</head>
<body>
  <div class="flyer">
    <div class="frame-top"></div>
    <div class="frame-right"></div>
    <div class="plate"></div>
    <div class="brand"><span class="brand-dot"></span>Tellerbund</div>

    <h1 class="headline headline-one">Je <strong>mehr</strong> bestellen,</h1>
    <p class="headline headline-two">desto <strong>günstiger</strong> wird’s</p>

    <ul class="benefits">
      <li><svg viewBox="0 0 24 24"><path d="M4 12l5 5L20 6" fill="none" stroke="#555" stroke-width="2.5" stroke-linecap="round" stroke-linejoin="round"/></svg>Keine Mindestbestellung</li>
      <li><svg viewBox="0 0 24 24"><path d="M4 12l5 5L20 6" fill="none" stroke="#555" stroke-width="2.5" stroke-linecap="round" stroke-linejoin="round"/></svg>Keine Lieferpauschal</li>
      <li><svg viewBox="0 0 24 24"><path d="M4 12l5 5L20 6" fill="none" stroke="#555" stroke-width="2.5" stroke-linecap="round" stroke-linejoin="round"/></svg>Essen und Punkte sammeln</li>
    </ul>

    <div class="cta">jetzt sparen</div>
    <svg class="cta-pointer" viewBox="0 0 22 34">
      <path d="M2 2 L2 26 L8 20 L13 31 L17 29 L12 19 L20 19 Z" fill="#fff" stroke="#222" stroke-width="1.6" stroke-linejoin="round"/>
    </svg>

    <div class="food-photo" role="img" aria-label="Foto eines gegrillten Panini mit grünem Salat"></div>
    <div class="pointer-crowd" role="img" aria-label="Viele Mauszeiger, die nach oben zur Schaltfläche streben"></div>

    <p class="web-address">www.tellerbund.ch</p>
  </div>
</body>
</html>
```